Tallow Grains Presents Dr Mira Coskett from Furrow Studies of Nevada

Tallow Grains is bringing Dr Mira Coskett from Furrow Studies of Nevada to Auckland for a one day only seminar. Dr Coskett is recognised as a world authority on turfgrass. Mira received her master's and Ph.D from the University of Varnholt where she first worked on heat tolerant bentgrasses and improved bermuda grasses. Mira's work reflects Harvest of Notions approach that drives product development. At Furrow Studies of Nevada, our emphasis is on producing grasses that can survive with less water, and are highly disease resistance, reducing or eliminating the need for fungicides and fertilizers. By interacting with superintendents and distributors, we determine their needs and then find solutions to satisfy the requirements of their projects.

Target Market(s)

Turf managers in New Zealand

Font styles to use
Serif

Colors

Designer to choose colors to be used in the design.

Requirements
Must have
• Date: Friday 31 August 2018 at Quorvel Harbourside Lodge, 10.30am until 3pm
• Morning tea served from 9.30am
• Free parking in Lot K
• Please let us know if you have any special dietary requirements
Nice to have
• All three logos, above information about Mira

```html
<!DOCTYPE html>
<html lang="en">
<head>
<meta charset="utf-8">
<title>Smart Solutions – Seminar Poster</title>
<link href="https://fonts.googleapis.com/css2?family=Oswald:wght@600&family=Arimo:wght@400;700&display=swap" rel="stylesheet">
<style>
  :root {
    --turf-green: #146b3a;
    --deep-green: #0f5a30;
    --clay-brown: #7a2e1c;
    --seed-red: #c8202f;
    --ink: #333333;
    --paper: #ffffff;
    --paper-shade: #f1f1f1;
    --backdrop: #e4e4e4;
  }
  * { margin: 0; padding: 0; box-sizing: border-box; }
  html, body { width: 1200px; height: 1200px; overflow: hidden; }
  body {
    background: var(--backdrop);
    font-family: "Arimo", Arial, sans-serif;
    color: var(--ink);
  }
  .poster {
    position: absolute;
    left: 207px; top: 50px;
    width: 785px; height: 1100px;
    background: linear-gradient(180deg, var(--paper) 0%, var(--paper-shade) 100%);
    overflow: hidden;
  }
  .poster-art { position: absolute; left: 0; top: 0; width: 785px; height: 1100px; }
  .headline {
    position: absolute; left: 0; right: 0; top: 498px;
    text-align: center;
    font-family: "Oswald", "Arial Narrow", sans-serif;
    font-weight: 600; font-size: 86px; line-height: 1;
    letter-spacing: -1px;
    color: var(--turf-green);
    transform: scaleX(0.92);
  }
  .tagline {
    position: absolute; left: 0; right: 0; top: 588px;
    text-align: center; font-size: 30px; line-height: 36px; letter-spacing: 0.3px;
    color: var(--ink);
  }
  .date-pill {
    position: absolute; left: 198px; top: 658px;
    width: 337px; height: 47px;
    background: var(--turf-green); color: var(--paper);
    border-radius: 9px;
    display: flex; align-items: center; justify-content: center;
    font-size: 26px; letter-spacing: 0.5px;
  }
  .venue {
    position: absolute; left: 0; right: 0; top: 723px;
    text-align: center; font-size: 22px; color: #222;
  }
  .venue strong { font-size: 32px; font-weight: 700; color: var(--clay-brown); margin-left: 4px; }
  .rule {
    position: absolute; left: 51px; width: 679px; height: 3px;
    background: var(--turf-green);
  }
  .rule-top { top: 802px; }
  .rule-bottom { top: 892px; }
  .times {
    position: absolute; top: 828px; height: 46px;
    display: flex; align-items: center; white-space: nowrap;
    font-size: 19px; color: #222;
  }
  .times b { font-size: 27px; font-weight: 700; color: var(--turf-green); margin: 0 5px; }
  .times-session { left: 68px; }
  .times-tea { left: 362px; }
  .times-divider {
    position: absolute; left: 332px; top: 827px;
    width: 2px; height: 52px; background: #777;
  }
  .notice {
    position: absolute; left: 0; right: 0; top: 905px;
    text-align: center; font-size: 16px; line-height: 20px; color: #222;
  }
  .notice b { color: var(--turf-green); }
  .partner {
    position: absolute; top: 940px; height: 88px;
    display: flex; flex-direction: column; align-items: center; justify-content: center;
    text-align: center; font-weight: 700; white-space: nowrap;
  }
  .partner-host { left: 50px; width: 190px; color: var(--turf-green); font-size: 20px; }
  .partner-host .mark {
    width: 34px; height: 34px; border-radius: 50%;
    background: var(--turf-green); margin-bottom: 6px;
  }
  .partner-research { left: 250px; width: 270px; color: var(--seed-red); font-size: 20px; line-height: 1.15; }
  .partner-research small { font-size: 14px; font-weight: 700; margin-top: 5px; }
  .partner-seeds { left: 540px; width: 200px; color: var(--ink); font-size: 21px;
    flex-direction: row; gap: 10px; }
  .partner-seeds .mark { width: 28px; height: 28px; background: var(--turf-green); }
  .footer {
    position: absolute; left: 0; right: 0; bottom: 0; height: 57px;
    background: var(--turf-green); color: var(--paper);
    display: flex; align-items: center; justify-content: center;
    font-size: 22px; letter-spacing: 0.3px;
  }
  .footer span { margin-left: 16px; }
</style>
</head>
<body>
<main class="poster">
  <svg class="poster-art" viewBox="0 0 826 1158" preserveAspectRatio="none">
    <defs>
      <linearGradient id="turfPhoto" x1="0" y1="0" x2="1" y2="1">
        <stop offset="0" stop-color="#2f8a1e"/>
        <stop offset="0.45" stop-color="#57b02a"/>
        <stop offset="1" stop-color="#3a8f1f"/>
      </linearGradient>
    </defs>
    <path role="img" aria-label="Photo: white rugby ball resting on a freshly mown green turf field"
          fill="url(#turfPhoto)"
          d="M0 0 H826 V382 C720 318 580 320 420 395 C270 465 130 470 0 392 Z"/>
    <path class="wave-band" fill="#146b3a"
          d="M0 392 C130 470 270 465 420 395 C580 320 720 318 826 382 L826 392 C720 340 590 345 430 420 C280 490 120 492 0 392 Z"/>
    <path class="wave-line" fill="none" stroke="#7a2e1c" stroke-width="4"
          d="M30 425 C150 500 290 492 440 425 C590 358 720 350 815 385"/>
  </svg>

  <h1 class="headline">SMART SOLUTIONS</h1>
  <p class="tagline">Extensive product range and expertise</p>
  <div class="date-pill">Friday, 31 August 2018</div>
  <p class="venue">at <strong>Quorvel Harbourside Lodge</strong></p>

  <div class="rule rule-top"></div>
  <p class="times times-session"><b>10.30am</b> until <b>3pm</b></p>
  <div class="times-divider"></div>
  <p class="times times-tea">Morning tea served from <b>9.30am</b></p>
  <div class="rule rule-bottom"></div>

  <p class="notice"><b>Free parking in Lot K</b> · Please let us know if you have any special dietary requirements</p>

  <div class="partner partner-host"><div class="mark"></div>Tallow Grains Turf</div>
  <div class="partner partner-research">Furrow Studies of Nevada<small>Harvest of Notions</small></div>
  <div class="partner partner-seeds"><div class="mark"></div>Kessel Seedworks</div>

  <footer class="footer">For more information visit:<span>www.tallowgrains.co.nz</span></footer>
</main>
</body>
</html>
```